Business card design needed

The company name is Pellwick Architects. We are an architectural company based in Melbourne,Australia that has a mix of client base from health care, commercial office, aged care, multi-residential, single residential and retail. Design type is contemporary.

Suggest the base colours need to be black and white. Please leave an area on the back of the card available for handwritten notes.

Target Market(s)

Generally corporate, aged 30 to 65

Industry/Entity Type

Residential

Contact Information for Business Card

Pellwick Architects
Dane Pellwick
7 Horbury Street
Northvale VIC 3059
T (03) 9572 4016
M 0431 607 295
E dp@pellwickarc.com.au

Logo Text

PA

Logo styles of interest
Emblem Logo
Abstract Logo
Lettermark Logo
Requirements
Must have
• I am having trouble attaching a sketch so would really appreciate your effort to try the following brief.

Black and White (B&W)
Would like different card cutout profile. Logo Example, use the half circle curve of the G to form the left edge of the card with no margin. The A is to sit inside the G, connected to the G by its horizontal. The A has its cross bar and lower right leg removed. Card in black, text in white.

Back of card to be black text on white background with services provided.

Client Focused Service
Architecture and Design
Functional Planning
Town Planning
Feasability Studies
Contract Documentation
Contract Administration
Project Management

Simple elegant text, Ariel or similar
Nice to have
• Integrated logo and card cut-out.

Card base black on front, white on back
Should not have
• Too many colours
Fussy details

```html
<!DOCTYPE html>
<html lang="en">
<head>
<meta charset="utf-8">
<title>Pellwick Architects – Business Card</title>
<link rel="stylesheet" href="https://fonts.googleapis.com/css2?family=Arimo:wght@400;700&display=swap">
<style>
  :root {
    --backdrop: #cccccc;
    --ink: #000000;
    --paper: #ffffff;
    --bullet: #8a8a8a;
  }
  html, body {
    margin: 0;
    padding: 0;
    width: 1200px;
    height: 1000px;
    overflow: hidden;
    background: var(--backdrop);
    font-family: "Arimo", Arial, sans-serif;
  }
  .canvas {
    position: relative;
    width: 1200px;
    height: 1000px;
  }
  .card-shapes {
    position: absolute;
    inset: 0;
  }
  .front-text {
    position: absolute;
    right: 357px;
    text-align: right;
    color: var(--paper);
    line-height: 1;
    margin: 0;
  }
  .company-name {
    top: 105px;
    font-size: 29px;
    font-weight: 700;
  }
  .person-name {
    top: 257px;
    font-size: 25px;
    font-weight: 700;
  }
  .contact-details {
    top: 319px;
    font-size: 20px;
    line-height: 25px;
    font-weight: 400;
  }
  .monogram {
    position: absolute;
    left: 250px;
    top: 222px;
    width: 200px;
    text-align: center;
    font-size: 88px;
    font-weight: 700;
    line-height: 1;
    color: var(--paper);
    margin: 0;
  }
  .services {
    position: absolute;
    left: 399px;
    top: 585px;
    color: var(--ink);
  }
  .services-heading {
    margin: 0 0 6px;
    font-size: 25px;
    font-weight: 700;
    line-height: 1;
  }
  .services-list {
    list-style: none;
    margin: 0;
    padding: 0 0 0 56px;
  }
  .services-list li {
    position: relative;
    font-size: 26px;
    line-height: 31.3px;
  }
  .services-list li::before {
    content: "";
    position: absolute;
    left: -44px;
    top: 9px;
    width: 11px;
    height: 11px;
    border: 1.5px solid var(--bullet);
    border-radius: 50%;
  }
</style>
</head>
<body>
<main class="canvas">
  <svg class="card-shapes" width="1200" height="1000" viewBox="0 0 1200 1000" aria-hidden="true">
    <!-- front card -->
    <rect class="front-card" x="350" y="61" width="521" height="412" fill="var(--ink)"/>
    <circle class="front-profile" cx="350" cy="267" r="208" fill="var(--paper)"/>
    <circle class="front-profile-inner" cx="350" cy="267" r="168" fill="var(--ink)"/>
    <!-- back card -->
    <path class="back-card" d="M344 508 H866 A205 205 0 0 1 866 918 H344 Z" fill="var(--paper)"/>
  </svg>

  <section class="card-front" aria-label="Card front">
    <p class="monogram">PA</p>
    <h1 class="front-text company-name">Pellwick Architects</h1>
    <h2 class="front-text person-name">Dane Pellwick</h2>
    <p class="front-text contact-details">
      7 Horbury Street<br>
      Northvale VIC 3059<br>
      T (03) 9572 4016<br>
      M 0431 607 295<br>
      E dp@pellwickarc.com.au
    </p>
  </section>

  <section class="card-back services" aria-label="Card back">
    <h3 class="services-heading">Client Focused Service</h3>
    <ul class="services-list">
      <li>Architecture and Design</li>
      <li>Functional Planning</li>
      <li>Town Planning</li>
      <li>Feasability Studies</li>
      <li>Contract Documentation</li>
      <li>Contract Administration</li>
      <li>Project Management</li>
    </ul>
  </section>
</main>
</body>
</html>
```